Peter Lasko-Wren Finance

Need a personal website advertising Equipment Finance,Business Finance,Commercial Finance, Construction Finance, Bridging Finance. Similar websites are www.varoplend.com.au / www.kitmoxa.com.au / www.rzb4.com.au /wwwbelvaxcredit.com.au

Target Market(s)

Business People

Industry/Entity Type

Business

Number of Pages Required

3 page

Font styles to use
Serif
Sans Serif

Requirements
Must have
• All i want is a simple corporate looking website advertising Equipment Finance, Commercial Finance, Construction Finance, Business Finance, Bridging Finance,

```html
<!DOCTYPE html>
<html lang="en">
<head>
<meta charset="utf-8">
<title>Peter Lasko-Wren Finance</title>
<link href="https://fonts.googleapis.com/css2?family=Lato:wght@300;400;700&family=Ubuntu:wght@400;500&family=Lora:wght@500&display=swap" rel="stylesheet">
<style>
:root{
  --dark:#2e2e2e;
  --blue:#5bb8e2;
  --blue-deep:#29a9e1;
  --accent:#1f95d1;
  --red:#d9363e;
  --grey-band:#e8e8e8;
  --light:#f4f4f4;
  --text:#333;
  --muted:#777;
  --white:#fff;
}
*{margin:0;padding:0;box-sizing:border-box}
html,body{width:1200px;height:3830px;overflow:hidden}
body{position:relative;background:var(--white);font-family:"Lato",sans-serif;color:var(--text)}
.abs{position:absolute}
.topbar{left:0;top:0;width:1200px;height:26px;background:var(--dark);color:var(--white);font-size:13px}
.topbar span{position:absolute;top:5px;display:flex;align-items:center;gap:6px}
.quick{position:absolute;left:983px;top:2px;width:115px;height:22px;background:var(--red);color:#fff;font-size:13px;text-align:center;line-height:22px}
.header{left:0;top:26px;width:1200px;height:94px;background:#fff}
.logo{position:absolute;left:102px;top:33px;width:255px;display:flex;align-items:center;gap:8px;font-family:"Lora",serif;font-weight:500;font-size:22px;line-height:28px;color:var(--accent);white-space:nowrap}
.logo i{width:12px;height:12px;border-radius:50%;background:var(--accent);display:block;flex:none}
.mainnav a{position:absolute;top:30px;height:38px;line-height:38px;font-size:14px;font-weight:700;color:var(--accent);text-decoration:none;padding:0 22px;letter-spacing:.5px}
.mainnav a.active{background:var(--dark);color:#fff}
.search{position:absolute;left:868px;top:30px;width:230px;height:34px;border:1px solid #bbb;background:#fff}
.search b{position:absolute;right:0;top:0;width:30px;height:32px;background:var(--dark)}
.subnav{left:0;top:120px;width:1200px;height:41px;background:var(--blue)}
.subnav span{position:absolute;top:12px;color:#fff;font-size:13px;font-weight:700;letter-spacing:.5px}
.hero{left:0;top:161px;width:1200px;height:554px;background:linear-gradient(120deg,#9aa4ad 0%,#d8dde2 45%,#eef0f2 70%,#7d8893 100%)}
.callback{left:350px;top:480px;width:492px;height:174px;background:rgba(235,235,235,.92);padding:14px 18px;font-family:Georgia,serif;font-size:14px;color:#444}
.callback .field{position:absolute;top:70px;width:228px;height:36px;background:#ddd;border:1px solid #bbb;font-size:13px;color:#777;padding:9px 10px}
.callback .go{position:absolute;left:18px;top:126px;padding:0 14px;height:32px;line-height:32px;background:var(--accent);color:#fff;font-size:13px;font-family:"Lato",sans-serif;font-weight:700}
.callback .apply{position:absolute;left:150px;top:132px;color:#e08a1e;font-size:13px}
.dots{left:545px;top:682px;display:flex;gap:12px}
.dots i{width:16px;height:16px;border-radius:50%;background:rgba(255,255,255,.75);display:block}
.dots i:first-child{background:var(--accent)}
.title{left:0;width:1200px;text-align:center;font-family:"Lato",sans-serif;font-weight:400;font-size:35px;letter-spacing:3px;color:#333}
.title::after{content:"";display:block;width:130px;height:4px;background:var(--accent);margin:18px auto 0}
.copy{left:102px;width:996px;font-size:14px;line-height:25px;letter-spacing:.6px;color:#333}
.btn{height:34px;line-height:34px;padding:0 16px;background:var(--dark);color:#fff;font-size:13px;font-weight:700;letter-spacing:1px}
.services{left:0;top:1085px;width:1200px;height:307px;background:var(--blue)}
.arrow{position:absolute;width:48px;height:48px;border-radius:50%;background:#eee;border:3px solid var(--dark)}
.svc{position:absolute;top:38px;width:220px;text-align:center}
.svc .pic{width:100px;height:88px;margin:0 auto;border-radius:8px}
.svc h3{font-family:"Ubuntu",sans-serif;font-weight:500;font-size:29px;color:#222;margin-top:10px;letter-spacing:1px}
.svc p{font-size:13px;font-weight:700;color:#fff;margin-top:2px}
.svc .btn{display:inline-block;margin-top:44px;height:26px;line-height:26px;font-size:11px}
.review{position:absolute;top:1572px;width:320px;text-align:center}
.avatar{width:100px;height:100px;border-radius:50%;margin:0 auto;background:radial-gradient(circle at 50% 40%,#d9b8a0,#8a6d5c 70%,#ccc 71%);border:3px solid #eee}
.review h4{font-size:11px;font-weight:400;color:var(--accent);margin-top:14px;letter-spacing:.5px;border-bottom:1px solid #ddd;padding-bottom:8px}
.review p{font-size:11px;line-height:15px;color:#444;margin-top:8px}
.review p a{color:var(--accent);text-decoration:none}
.gallery{left:0;top:1902px;width:1200px;height:536px;background:var(--grey-band)}
.card{position:absolute;top:71px;width:312px}
.card .pic{height:248px;position:relative}
.card .pic span{position:absolute;left:0;bottom:0;width:100%;height:40px;line-height:42px;background:rgba(40,40,40,.6);color:#fff;text-align:center;font-family:"Ubuntu",sans-serif;font-size:20px;letter-spacing:2px}
.card p{font-size:14px;line-height:23px;letter-spacing:.4px;margin-top:16px;text-align:justify}
.card .btn{position:absolute;left:86px;top:378px;height:30px;line-height:30px}
.partners{left:0;top:2910px;width:1200px;height:294px;background:var(--blue-deep)}
.partners .lead{position:absolute;top:36px;width:1200px;text-align:center;color:#fff;font-size:13px}
.plogo{position:absolute;top:72px;width:227px;height:163px;background:#fff;display:flex;align-items:center;justify-content:center;gap:10px;font-family:"Lato",sans-serif;font-weight:700;font-size:16px;color:#2a4a6b;text-align:center}
.plogo i{width:22px;height:22px;background:#2a4a6b;display:block;flex:none}
.contact{left:0;top:3204px;width:1200px;height:541px;background:var(--light)}
.inp{position:absolute;background:#fff;border:1px solid #999;font-size:14px;color:#999;padding:12px 16px}
.submit{position:absolute;left:620px;top:263px;width:466px;height:46px;line-height:46px;background:var(--dark);color:#fff;text-align:center;font-weight:700;font-size:14px;letter-spacing:1px}
.info{position:absolute;top:370px;width:300px;text-align:center}
.info h5{font-size:22px;font-weight:400;letter-spacing:1px;color:#333;margin-top:12px}
.info p{font-size:14px;line-height:20px;color:#555;margin-top:4px}
.footer{left:0;top:3745px;width:1200px;height:85px;background:var(--dark);color:#fff;font-size:13px}
.footer .social{position:absolute;left:854px;top:24px;display:flex;gap:12px}
.footer .social i{width:38px;height:38px;border-radius:50%;background:#fff;display:block}
</style>
</head>
<body>

<div class="abs topbar">
  <span style="left:102px"><svg width="16" height="12" viewBox="0 0 16 12"><rect x="1" y="1" width="14" height="10" fill="none" stroke="#fff" stroke-width="1.5"/><path d="M1 1l7 6 7-6" fill="none" stroke="#fff" stroke-width="1.5"/></svg>contact@laskowren.com</span>
  <span style="left:541px"><svg width="12" height="14" viewBox="0 0 12 14"><path d="M2 1l3 0 1 3-2 1c1 2 2 3 4 4l1-2 3 1 0 3c-6 1-11-4-10-10z" fill="#fff"/></svg>+1 555 010 2244</span>
  <div class="quick">Quick Quote</div>
</div>

<header class="abs header">
  <div class="logo"><i></i>PETER LASKO-WREN</div>
  <nav class="mainnav">
    <a class="active" style="left:375px">HOME</a>
    <a style="left:476px">ABOUT</a>
    <a style="left:570px">SERVICES</a>
    <a style="left:686px">KEY PEOPLE</a>
  </nav>
  <div class="search"><b><svg width="30" height="32" viewBox="0 0 30 32"><circle cx="13" cy="14" r="6" fill="none" stroke="#fff" stroke-width="2"/><path d="M17 18l6 6" stroke="#fff" stroke-width="2.5"/></svg></b></div>
</header>

<nav class="abs subnav">
  <span style="left:100px">BUSINESS FINANCE</span>
  <span style="left:294px">COMMERCIAL FINANCE</span>
  <span style="left:505px">CONSTRUCTION FINANCE</span>
  <span style="left:748px">INSURANCE</span>
  <span style="left:873px">HOW IT WORKS</span>
  <span style="left:1029px">CONTACT</span>
</nav>

<div class="abs hero" role="img" aria-label="Photo of a businessman signing documents with a pen beside a laptop"></div>
<form class="abs callback">
  Get Funded Today, enter details below for a call back
  <div class="field" style="left:18px">Phone Number</div>
  <div class="field" style="left:246px">Email Address</div>
  <div class="go">Get A Call Back</div>
  <div class="apply">[Apply online]</div>
</form>
<div class="abs dots"><i></i><i></i><i></i><i></i></div>

<h2 class="abs title" style="top:765px">BUSINESS FINANCE</h2>
<p class="abs copy" style="top:872px">Lorem Ipsum is simply dummy text of the printing and typesetting industry. Lorem Ipsum has been the industry's standard dummy text ever since the 1500s, when an unknown printer took a galley of type and scrambled it to make a type specimen book. It has survived not only five centuries, but also the leap into electronic typesetting,...</p>
<div class="abs btn" style="left:546px;top:983px">READ MORE</div>

<section class="abs services">
  <div class="arrow" style="left:22px;top:116px"><svg width="42" height="42" viewBox="0 0 42 42"><path d="M25 12l-10 9 10 9z" fill="#2e2e2e"/></svg></div>
  <div class="arrow" style="left:1122px;top:116px"><svg width="42" height="42" viewBox="0 0 42 42"><path d="M17 12l10 9-10 9z" fill="#2e2e2e"/></svg></div>
  <div class="svc" style="left:102px"><div class="pic" role="img" aria-label="Megaphone illustration" style="background:linear-gradient(#e9e9e9,#c43a3a)"></div><h3>Marketing</h3><p>Lorem Ipsum is simply</p><span class="btn">READ MORE</span></div>
  <div class="svc" style="left:350px"><div class="pic" role="img" aria-label="Organisation structure illustration" style="background:linear-gradient(#a64532,#6e2a1e)"></div><h3>Structure</h3><p>Lorem Ipsum is simply</p><span class="btn">READ MORE</span></div>
  <div class="svc" style="left:623px"><div class="pic" role="img" aria-label="Bank building with coins illustration" style="background:linear-gradient(#e8c65a,#b7a27a)"></div><h3>Banking</h3><p>Lorem Ipsum is simply</p><span class="btn">READ MORE</span></div>
  <div class="svc" style="left:878px"><div class="pic" role="img" aria-label="Light bulb illustration" style="background:linear-gradient(#f0a541,#44627a)"></div><h3>Consulting</h3><p>Lorem Ipsum is simply</p><span class="btn">READ MORE</span></div>
</section>

<h2 class="abs title" style="top:1448px;font-size:30px">SEE SOME OF THE REVIEWS HERE</h2>
<div class="review" style="left:82px"><div class="avatar" role="img" aria-label="Portrait photo of reviewer"></div><h4>DALE MARSH, IRONLEAF WEB</h4><p>"We can build more robust sites faster. That impacts both cost and value. We can roll out powerful sites for lower budgets and clear a nice profit as an agency."<br><a>Read their story »</a></p></div>
<div class="review" style="left:440px"><div class="avatar" role="img" aria-label="Portrait photo of reviewer"></div><h4>OWEN PETRIE, QUIET ORCHARD</h4><p>"Your business online is about more than just a website. Using Launchdeck, we focus on Digital Marketing and Search Engine Optimization to maximize returns."<br><a>Read their story »</a></p></div>
<div class="review" style="left:796px"><div class="avatar" role="img" aria-label="Portrait photo of reviewer"></div><h4>LUKE FARROW, STUDIO KESTREL</h4><p>"The decision to become a Partner has been a brilliant move. We now have all the tools we need and the confidence to move forward and grow our business."<br><a>Read their story »</a></p></div>
<div class="abs btn" style="left:542px;top:1831px">VIEW MORE</div>

<section class="abs gallery">
  <div class="card" style="left:102px"><div class="pic" role="img" aria-label="Photo of a handshake in front of glass office towers" style="background:linear-gradient(160deg,#5d86b5,#b9c8d8 60%,#6f6f6f)"><span>COMMERCIAL</span></div><p>Lorem Ipsum is simply dummy text of the printing andtypesetting industry. Lorem Ipsum has been the industry's standard dummy text ever since the 1500s,</p><span class="btn">READ MORE</span></div>
  <div class="card" style="left:444px"><div class="pic" role="img" aria-label="Photo of a business team meeting around a table" style="background:linear-gradient(160deg,#c9ccd0,#8e9aa6 60%,#5b6570)"><span>CONSTRUCTION</span></div><p>Lorem Ipsum is simply dummy text of the printing andtypesetting industry. Lorem Ipsum has been the industry's standard dummy text ever since the 1500s,</p><span class="btn">READ MORE</span></div>
  <div class="card" style="left:789px"><div class="pic" role="img" aria-label="Photo of a business team meeting around a table" style="background:linear-gradient(160deg,#c9ccd0,#8e9aa6 60%,#5b6570)"><span>INSURANCE</span></div><p>Lorem Ipsum is simply dummy text of the printing andtypesetting industry. Lorem Ipsum has been the industry's standard dummy text ever since the 1500s,</p><span class="btn">READ MORE</span></div>
</section>

<h2 class="abs title" style="top:2496px;font-size:30px">PROFESSIONAL SERVICE FROM AN AWARD WINNING TEAM</h2>
<p class="abs copy" style="top:2589px">Lorem Ipsum is simply dummy text of the printing and typesetting industry. Lorem Ipsum has been the industry's standard dummy text ever since the 1500s, when an unknown printer took a galley of type and scrambled it to make a type specimen book. It has survived not only five centuries, but also the leap into electronic typesetting,...</p>
<p class="abs copy" style="top:2676px">Lorem Ipsum is simply dummy text of the printing and typesetting industry. Lorem Ipsum has been the industry.<br>dummy text ever since the 1500s,<br>when an unknown printer took a galley of type and<br>scrambled it to make a type specimen</p>
<div class="abs btn" style="left:538px;top:2819px">READ MORE</div>

<section class="abs partners">
  <div class="lead">We compare loan and insurance products from some of Australia's leading finance and insurance companies.</div>
  <div class="arrow" style="left:14px;top:127px;width:46px;height:46px;background:#fff;border:3px solid #9ad4ef"><svg width="40" height="40" viewBox="0 0 40 40"><path d="M24 12l-9 8 9 8" fill="none" stroke="#29a9e1" stroke-width="4"/></svg></div>
  <div class="arrow" style="left:1128px;top:127px;width:46px;height:46px;background:#fff;border:3px solid #9ad4ef"><svg width="40" height="40" viewBox="0 0 40 40"><path d="M16 12l9 8-9 8" fill="none" stroke="#29a9e1" stroke-width="4"/></svg></div>
  <div class="plogo" style="left:102px"><i></i>LEDGERLINE REVIEW</div>
  <div class="plogo" style="left:358px"><i></i>NUMERA STATS</div>
  <div class="plogo" style="left:615px"><i></i>HOLT VARGA CPA</div>
  <div class="plogo" style="left:873px"><i></i>COMPANY NAME</div>
</section>

<section class="abs contact">
  <h2 class="abs title" style="top:52px;font-size:24px;font-weight:700;letter-spacing:2px">SEND A MESSAGE</h2>
  <div class="inp" style="left:115px;top:135px;width:477px;height:46px">Your Name</div>
  <div class="inp" style="left:115px;top:199px;width:477px;height:46px">Your Email</div>
  <div class="inp" style="left:115px;top:263px;width:477px;height:46px">Subject</div>
  <div class="inp" style="left:620px;top:135px;width:466px;height:108px">Your Message</div>
  <div class="submit">SUBMIT</div>
  <div class="info" style="left:103px">
    <svg width="52" height="52" viewBox="0 0 52 52"><circle cx="26" cy="26" r="24" fill="none" stroke="#1f95d1" stroke-width="3"/><path d="M14 27l12-11 12 11M18 24v12h16V24" fill="none" stroke="#1f95d1" stroke-width="3"/></svg>
    <h5>OUR ADRESS</h5><p>4870 Harbour Lane,<br>Suite 312</p>
  </div>
  <div class="info" style="left:455px">
    <svg width="52" height="52" viewBox="0 0 52 52"><circle cx="26" cy="26" r="24" fill="none" stroke="#1f95d1" stroke-width="3"/><rect x="14" y="18" width="24" height="16" fill="none" stroke="#1f95d1" stroke-width="3"/><path d="M14 18l12 9 12-9" fill="none" stroke="#1f95d1" stroke-width="3"/></svg>
    <h5>OUR EMAIL</h5><p>email@yourdomain.com</p>
  </div>
  <div class="info" style="left:815px">
    <svg width="52" height="52" viewBox="0 0 52 52"><circle cx="26" cy="26" r="24" fill="none" stroke="#1f95d1" stroke-width="3"/><path d="M17 14h6l2 6-3 2c2 4 4 6 8 8l2-3 6 2v6c-12 1-22-9-21-21z" fill="#1f95d1"/></svg>
    <h5>CALL US</h5><p>+1 (0) 101 0000 000</p>
  </div>
</section>

<footer class="abs footer">
  <div class="abs" style="left:102px;top:33px">Copyright © 2017 <b>Peter Lasko-Wren</b>. All Rights Reserved.</div>
  <div class="social"><i></i><i></i><i></i><i></i><i></i></div>
</footer>

</body>
</html>
```